Informative brochure for college admissions prep service

Take the attached prose and images and design an attractive brochure. The color scheme should use the Marlowe University colors (black, cardinal, and white). The photos should all be grey scaled.

Cardinal

```html
<!DOCTYPE html>
<html lang="en">
<head>
<meta charset="utf-8">
<title>Our Admissions Mentors</title>
<link href="https://fonts.googleapis.com/css2?family=Nunito+Sans:wght@400;700&display=swap" rel="stylesheet">
<style>
  :root {
    --paper: #ffffff;
    --ink: #111111;
    --cardinal: #8c1c1f;
    --band-deep: #5e0b0e;
    --band-mid: #7d1317;
    --band-bright: #a0262a;
    --grey-1: #e6e6e6;
    --grey-2: #c4c4c4;
    --grey-3: #9a9a9a;
    --grey-4: #6c6c6c;
    --grey-5: #3c3c3c;
    --grey-6: #1f1f1f;
  }
  html, body {
    margin: 0;
    padding: 0;
    overflow: hidden;
  }
  body {
    width: 927px;
    height: 1200px;
    background: var(--paper);
    font-family: "Nunito Sans", Arial, sans-serif;
    position: relative;
  }
  .mentor-grid {
    position: absolute;
    top: 111px;
    left: 107px;
    display: grid;
    grid-template-columns: repeat(3, 190px);
    column-gap: 71px;
    grid-auto-rows: 325px;
  }
  .mentor {
    display: flex;
    flex-direction: column;
    align-items: center;
    text-align: center;
  }
  .mentor--last {
    grid-column: 2;
  }
  .mentor__photo {
    width: 190px;
    height: 190px;
    flex: none;
  }
  .mentor__photo--theo {
    background:
      radial-gradient(ellipse 38% 34% at 50% 38%, var(--grey-2), transparent 70%),
      linear-gradient(180deg, var(--grey-1) 0%, var(--grey-2) 55%, var(--grey-5) 78%, var(--grey-6) 100%);
  }
  .mentor__photo--elias {
    background:
      radial-gradient(ellipse 36% 40% at 48% 45%, var(--grey-3), transparent 72%),
      linear-gradient(90deg, var(--grey-2) 0%, var(--grey-3) 45%, var(--grey-4) 80%, var(--grey-5) 100%);
  }
  .mentor__photo--jordan {
    background:
      radial-gradient(ellipse 34% 38% at 52% 48%, var(--grey-4), transparent 72%),
      linear-gradient(180deg, var(--grey-1) 0%, var(--grey-2) 60%, var(--grey-3) 100%);
  }
  .mentor__photo--reid {
    background:
      radial-gradient(ellipse 36% 40% at 50% 45%, var(--grey-3), transparent 72%),
      linear-gradient(180deg, var(--grey-3) 0%, var(--grey-2) 50%, var(--grey-1) 100%);
  }
  .mentor__photo--nadia {
    background:
      radial-gradient(ellipse 34% 36% at 45% 55%, var(--grey-2), transparent 72%),
      linear-gradient(120deg, var(--grey-3) 0%, var(--grey-5) 50%, var(--grey-6) 100%);
  }
  .mentor__photo--noel {
    background:
      radial-gradient(ellipse 30% 38% at 42% 50%, var(--grey-2), transparent 72%),
      linear-gradient(180deg, var(--grey-4) 0%, var(--grey-4) 70%, var(--grey-6) 100%);
  }
  .mentor__photo--clara {
    background:
      radial-gradient(ellipse 30% 40% at 48% 52%, var(--grey-2), transparent 72%),
      linear-gradient(90deg, var(--grey-4) 0%, var(--grey-3) 40%, var(--grey-5) 100%);
  }
  .mentor__name {
    margin: 15px 0 3px;
    font-size: 20px;
    font-weight: 700;
    color: var(--ink);
    line-height: 25px;
  }
  .mentor__school {
    margin: 0;
    font-size: 20px;
    font-weight: 400;
    color: var(--cardinal);
    line-height: 25px;
  }
  .footer-band {
    position: absolute;
    left: 0;
    bottom: 0;
    width: 927px;
    height: 132px;
    background:
      radial-gradient(ellipse 18% 60% at 8% 30%, rgba(160, 38, 42, 0.8), transparent 70%),
      radial-gradient(ellipse 22% 70% at 30% 80%, rgba(94, 11, 14, 0.7), transparent 70%),
      radial-gradient(ellipse 20% 60% at 55% 25%, rgba(160, 38, 42, 0.6), transparent 70%),
      radial-gradient(ellipse 24% 70% at 78% 70%, rgba(94, 11, 14, 0.7), transparent 70%),
      radial-gradient(ellipse 16% 55% at 95% 20%, rgba(160, 38, 42, 0.7), transparent 70%),
      var(--band-mid);
  }
</style>
</head>
<body>
  <main class="mentor-grid">
    <article class="mentor">
      <div class="mentor__photo mentor__photo--theo" role="img" aria-label="Greyscale portrait of Theo Varrick"></div>
      <h2 class="mentor__name">Theo Varrick</h2>
      <p class="mentor__school">Ashbury University<br>Hudsonia University</p>
    </article>
    <article class="mentor">
      <div class="mentor__photo mentor__photo--elias" role="img" aria-label="Greyscale portrait of Elias Dornfeld"></div>
      <h2 class="mentor__name">Elias Dornfeld</h2>
      <p class="mentor__school">University of<br>Keystone</p>
    </article>
    <article class="mentor">
      <div class="mentor__photo mentor__photo--jordan" role="img" aria-label="Greyscale portrait of Jordan Alcott"></div>
      <h2 class="mentor__name">Jordan Alcott</h2>
      <p class="mentor__school">Larkfield University</p>
    </article>
    <article class="mentor">
      <div class="mentor__photo mentor__photo--reid" role="img" aria-label="Greyscale portrait of Reid Hollis"></div>
      <h2 class="mentor__name">Reid Hollis</h2>
      <p class="mentor__school">Pinecrest State<br>Elmhaven University</p>
    </article>
    <article class="mentor">
      <div class="mentor__photo mentor__photo--nadia" role="img" aria-label="Greyscale portrait of Nadia Kowalin"></div>
      <h2 class="mentor__name">Nadia Kowalin</h2>
      <p class="mentor__school">Calloway University</p>
    </article>
    <article class="mentor">
      <div class="mentor__photo mentor__photo--noel" role="img" aria-label="Greyscale portrait of Noel Ashby"></div>
      <h2 class="mentor__name">Noel Ashby</h2>
      <p class="mentor__school">University of<br>Westmoor, Bayside</p>
    </article>
    <article class="mentor mentor--last">
      <div class="mentor__photo mentor__photo--clara" role="img" aria-label="Greyscale portrait of Clara Winsett Doyle"></div>
      <h2 class="mentor__name">Clara Winsett Doyle</h2>
      <p class="mentor__school">Ashbury University</p>
    </article>
  </main>
  <footer class="footer-band" role="img" aria-label="Cardinal red band with a faint pattern of leaves and branches"></footer>
</body>
</html>
```